Fine Art business needs new website

We need a simple website with a home page, about us page, New sculptures, Sold sculptures, and a contact us page.Our sculptures are very high end one of a kind pieces. As such we need the site to be VERY elegant and professional. Lastly, because I'll be updating pictures on the website on a monthly basis it needs to be user friendly to update (Wordpress is preferred). The only branding we have so far for the business is a business card.
Updates
I wasn't completely ready when this project launched, also I am on the road right now and haven't been able to be as responsive to all you designers as I would like. I will work on giving feedback to all the top designs we've received so far. Thank you all so much for your participation and hardwork.
Target Market(s)
High end customers (affluent), art collectors, interior decorators/designers
Industry/Entity Type
Art Gallery
Coding
Coded - Design and coding required
Number of Pages Required
5+ page
Requirements
Must have
- Easily editable picture gallery for myself so that I can add new pieces(pictures of the pieces), remove sold pieces, etc. I would like the website to be built in wordpress so I can update it. I currently use sitekeeperpro through Netbirch for my other business website and would like to do the same for this one.
- Pages:
- -Intro page with featured pieces
- -Current pieces gallery (for sale) mainly a picture gallery
- -Sculptures archive (sold pieces) another picture gallery
- -About us: Pull-down of -about the artist (attached content)
- -Artistic Process (attached content)
- -Show Schedule:
- -one page dedicated to "friends of QMW" (basically a link page)
- TO BE CLEAR "www.lanternhollow.com" IS A TOTALLY DIFFERENT SITE AND I'M NOT TRYING TO COMBINE THE TWO OR JOIN THEM INTO ONE. This page needs be more elegant and seperate from the Lantern Hollow site.
- UPDATE: I'd like a link to the QMW Facebook page: https://www.facebook.com/quillmarkworks/
Nice to have
- I would like the pictures on the gallery pages able to have text connected with them (Materials, price)
- I would like the site style and fonts to be similar to our business cards we've already had designed (picture attached).
Should not have
- Too much flash or other things that will make the site slow to load.

```html
<!DOCTYPE html>
<html lang="en">
<head>
<meta charset="utf-8">
<title>Quill Mark Works — Home</title>
<link rel="stylesheet" href="https://fonts.googleapis.com/css2?family=EB+Garamond:wght@400;500&display=swap">
<style>
  :root {
    --page-bg: #ffffff;
    --ink: #2b2b2b;
    --ink-soft: #555555;
    --hero-light: #f3f2f4;
    --hero-mist: #d9cfe4;
    --hero-violet: #8a67b4;
    --hero-deep: #4a2f72;
    --dot-idle: #b8b8b8;
    --dot-active: #5a5a5a;
    --card-bg: #111111;
    --label-bg: #ffffff;
    --price-bg: #d4d4d4;
    --stone-violet: #5b3f86;
    --stone-gold: #b89a5c;
    --stone-green: #1f6b48;
    --stone-teal: #7fb8a0;
  }

  * { box-sizing: border-box; margin: 0; padding: 0; }

  html, body {
    width: 1200px;
    height: 626px;
    overflow: hidden;
    background: var(--page-bg);
  }

  body {
    font-family: "EB Garamond", "Garamond", serif;
    color: var(--ink);
  }

  .site {
    width: 1200px;
    height: 626px;
    display: flex;
    flex-direction: column;
    align-items: center;
  }

  .site-header {
    padding-top: 18px;
    text-align: center;
  }

  .site-title {
    font-weight: 400;
    font-size: 28px;
    line-height: 1.1;
    letter-spacing: 1.5px;
    text-transform: uppercase;
  }

  .main-nav { margin-top: 12px; }

  .main-nav ul {
    display: flex;
    gap: 30px;
    list-style: none;
    justify-content: center;
  }

  .main-nav a {
    display: inline-block;
    font-size: 11px;
    letter-spacing: 0.6px;
    text-transform: uppercase;
    text-decoration: none;
    color: var(--ink-soft);
    padding-bottom: 3px;
  }

  .main-nav a.is-current {
    color: var(--ink);
    border-bottom: 2px solid var(--ink);
  }

  .hero {
    position: relative;
    width: 1148px;
    height: 230px;
    margin-top: 12px;
  }

  .hero-photo {
    position: absolute;
    inset: 0;
    background:
      radial-gradient(ellipse 38% 40% at 30% 55%, var(--hero-violet) 0%, rgba(138,103,180,0) 100%),
      radial-gradient(ellipse 30% 30% at 78% 85%, var(--hero-deep) 0%, rgba(74,47,114,0) 100%),
      var(--hero-light);
  }

  .hero-tagline {
    position: absolute;
    top: 24px;
    right: 40px;
    text-align: right;
    font-weight: 400;
    font-size: 20px;
    line-height: 1.05;
    letter-spacing: 0.6px;
    text-transform: uppercase;
  }

  .slider-dots {
    display: flex;
    gap: 10px;
    list-style: none;
    margin-top: 12px;
  }

  .slider-dots li {
    width: 7px;
    height: 7px;
    background: var(--dot-idle);
    transform: rotate(45deg);
  }

  .slider-dots li.is-active { background: var(--dot-active); }

  .featured {
    width: 1148px;
    margin-top: 14px;
    text-align: center;
  }

  .featured-title {
    font-weight: 400;
    font-size: 22px;
    letter-spacing: 0.8px;
    text-transform: uppercase;
  }

  .piece-grid {
    display: grid;
    grid-template-columns: repeat(4, 1fr);
    gap: 8px;
    margin-top: 12px;
    list-style: none;
  }

  .piece {
    position: relative;
    height: 206px;
    background: var(--card-bg);
    overflow: hidden;
  }

  .piece-photo {
    position: absolute;
    left: 22%;
    right: 22%;
    top: 18px;
    bottom: 0;
    border-radius: 46% 40% 8% 8%;
  }

  .piece-photo.is-violet {
    background: radial-gradient(circle at 55% 45%, var(--stone-gold) 0%, var(--stone-violet) 45%, var(--card-bg) 100%);
  }

  .piece-photo.is-green {
    background: radial-gradient(circle at 50% 40%, var(--stone-teal) 0%, var(--stone-green) 50%, var(--card-bg) 100%);
  }

  .piece-label {
    position: absolute;
    top: 10px;
    left: 10px;
    text-align: left;
  }

  .piece-name {
    display: block;
    background: var(--label-bg);
    color: var(--ink);
    font-size: 10px;
    font-weight: 500;
    letter-spacing: 0.4px;
    text-transform: uppercase;
    padding: 3px 8px;
  }

  .piece-price {
    display: inline-block;
    background: var(--price-bg);
    color: var(--ink);
    font-size: 10px;
    padding: 2px 8px;
    margin-top: 3px;
  }
</style>
</head>
<body>
  <div class="site">
    <header class="site-header">
      <h1 class="site-title">Quill Mark Works</h1>
      <nav class="main-nav" aria-label="Main">
        <ul>
          <li><a class="is-current" href="#">Home</a></li>
          <li><a href="#">About Us</a></li>
          <li><a href="#">Current Pieces</a></li>
          <li><a href="#">Sculptures Archive</a></li>
          <li><a href="#">Lantern Hollow</a></li>
          <li><a href="#">Contact Us</a></li>
        </ul>
      </nav>
    </header>

    <section class="hero">
      <div class="hero-photo" role="img" aria-label="Featured sculpture: a long arching amethyst crystal cluster on a light grey backdrop"></div>
      <h2 class="hero-tagline">Beauty at its<br>hardest expression</h2>
    </section>

    <ul class="slider-dots" aria-label="Slides">
      <li class="is-active"></li>
      <li></li>
      <li></li>
      <li></li>
    </ul>

    <section class="featured">
      <h2 class="featured-title">Current Pieces</h2>
      <ul class="piece-grid">
        <li class="piece">
          <div class="piece-photo is-violet" role="img" aria-label="Amethyst geode sculpture on a gold stand against black"></div>
          <div class="piece-label"><span class="piece-name">Product Name</span><span class="piece-price">$2950</span></div>
        </li>
        <li class="piece">
          <div class="piece-photo is-green" role="img" aria-label="Green malachite stone sculpture against black"></div>
          <div class="piece-label"><span class="piece-name">Product Name</span><span class="piece-price">$2950</span></div>
        </li>
        <li class="piece">
          <div class="piece-photo is-violet" role="img" aria-label="Amethyst geode sculpture on a gold stand against black"></div>
          <div class="piece-label"><span class="piece-name">Product Name</span><span class="piece-price">$2950</span></div>
        </li>
        <li class="piece">
          <div class="piece-photo is-green" role="img" aria-label="Green malachite stone sculpture against black"></div>
          <div class="piece-label"><span class="piece-name">Product Name</span><span class="piece-price">$2950</span></div>
        </li>
      </ul>
    </section>
  </div>
</body>
</html>
```